Unique Brovek Building Bussiness Card Design

www.brovek.com.au

Please see website for Company profile. We require a design that incorporates our logo colours and is unique in shape and style compared to all other business cards.

www.brovek.com.au

INSPIRE US !!!
Updates

Target Market(s)

Facility managers, Building Managers, Architects

Industry/Entity Type

Business

Contact Information for Business Card

Brovek Property Works
Project Manager
Dalton Pryseworth
0437 916 248
Sales@brovek.com.au

Logo Text

Brovek Property Works

Logo styles of interest
Abstract Logo
Requirements
Nice to have
• Card must show we are an established big business to trust.

```html
<!DOCTYPE html>
<html lang="en">
<head>
<meta charset="utf-8">
<title>Brovek Property Works – Business Card</title>
<link href="https://fonts.googleapis.com/css2?family=Open+Sans:wght@400;700&display=swap" rel="stylesheet">
<style>
  :root {
    --bg: #3a3d40;
    --card: #ffffff;
    --gold-light: #d9b43a;
    --gold-mid: #b8901c;
    --gold-dark: #7a5a0c;
    --edge: #111111;
    --ink: #111111;
    --brand: #1f3f73;
  }
  html, body {
    margin: 0;
    width: 1200px;
    height: 1000px;
    overflow: hidden;
    background: var(--bg);
    font-family: "Open Sans", Arial, sans-serif;
  }
  .canvas {
    position: relative;
    width: 1200px;
    height: 1000px;
  }
  .card {
    position: absolute;
    top: 335px;
    width: 540px;
    height: 320px;
  }
  .card--front { left: 40px; }
  .card--back { left: 620px; }
  .card svg { display: block; width: 540px; height: 320px; }
  .edge-line {
    fill: none;
    stroke: var(--edge);
    stroke-width: 5;
  }
  .brand-name {
    position: absolute;
    left: 90px;
    top: 128px;
    display: flex;
    align-items: center;
    gap: 14px;
    font-weight: 700;
    font-size: 40px;
    color: var(--brand);
    letter-spacing: 0.5px;
  }
  .brand-mark {
    width: 26px;
    height: 26px;
    background: var(--brand);
  }
  .contact {
    position: absolute;
    right: 22px;
    bottom: 24px;
    margin: 0;
    text-align: right;
    font-size: 17px;
    line-height: 1.2;
    color: var(--ink);
  }
</style>
</head>
<body>
<main class="canvas">

  <section class="card card--front" aria-label="Card front">
    <svg viewBox="0 0 540 320" xmlns="http://www.w3.org/2000/svg">
      <defs>
        <linearGradient id="goldFront" x1="0" y1="0" x2="1" y2="1">
          <stop offset="0" stop-color="var(--gold-light)"/>
          <stop offset="0.5" stop-color="var(--gold-mid)"/>
          <stop offset="1" stop-color="var(--gold-dark)"/>
        </linearGradient>
        <clipPath id="shapeFront">
          <path d="M0 0 H510 A30 30 0 0 1 540 30 V320 H30 A30 30 0 0 1 0 290 Z"/>
        </clipPath>
      </defs>
      <g clip-path="url(#shapeFront)">
        <rect class="card-face" width="540" height="320" fill="var(--card)"/>
        <path class="gold-band" role="img" aria-label="Gold woven texture band" d="M40 0 H540 V146 C380 64 220 36 40 0 Z" fill="url(#goldFront)"/>
        <path class="edge-line" d="M40 6 C220 42 380 70 540 153"/>
        <path class="gold-band" role="img" aria-label="Gold woven texture band" d="M0 232 C150 205 330 215 540 310 V320 H0 Z" fill="url(#goldFront)"/>
        <path class="edge-line" d="M0 225 C150 198 330 208 540 303"/>
      </g>
    </svg>
    <div class="brand-name"><span class="brand-mark"></span>brovek.com.au</div>
  </section>

  <section class="card card--back" aria-label="Card back">
    <svg viewBox="0 0 540 320" xmlns="http://www.w3.org/2000/svg">
      <defs>
        <linearGradient id="goldBack" x1="0" y1="0" x2="1" y2="1">
          <stop offset="0" stop-color="var(--gold-light)"/>
          <stop offset="0.5" stop-color="var(--gold-mid)"/>
          <stop offset="1" stop-color="var(--gold-dark)"/>
        </linearGradient>
        <clipPath id="shapeBack">
          <path d="M0 0 H510 A30 30 0 0 1 540 30 V320 H30 A30 30 0 0 1 0 290 Z"/>
        </clipPath>
      </defs>
      <g clip-path="url(#shapeBack)">
        <rect class="card-face" width="540" height="320" fill="var(--card)"/>
        <path class="gold-band" role="img" aria-label="Gold woven texture band" d="M158 0 H540 V114 C300 86 235 38 158 0 Z" fill="url(#goldBack)"/>
        <path class="edge-line" d="M148 2 C228 44 296 93 540 121"/>
        <path class="gold-band" role="img" aria-label="Gold woven texture band" d="M0 238 C76 242 142 274 216 320 H0 Z" fill="url(#goldBack)"/>
        <path class="edge-line" d="M0 231 C80 235 148 268 226 320"/>
      </g>
    </svg>
    <p class="contact">
      Brovek Property Works<br>
      Project Manager Dalton Pryseworth<br>
      0437 916 248 Sales@brovek.com.au
    </p>
  </section>

</main>
</body>
</html>
```